現在ラクトフェリンのサプリを販売しており新たに乳酸菌サプリを販売予定です。
https://mireloka.co.jp/
乳酸菌をイメージできオーガニックな感じを希望します。
胃溶性と腸容性の2種類のタイプのカプセルを選べるようにしており「胃で溶けるタイプ」と「腸まで届くタイプ」があります。
デザインの配置は当社のラクトフェリンのサプリと違っても構いません。
サプリの詳しい説明などは不要です。
既成の乳酸菌サプリにはないようなデザインを希望します。
■ラベルサイズ:W80mm×H90mm
■袋のサイズ:W110mm×H170mm
■印刷:オンデマンド
■色:4色(フルカラー)
■紙:ユポ紙80
記載項目
名称:クリスパタス菌+ガセリ菌 生きた乳酸菌100憶
カプセルのタイプ:「胃で溶けるタイプ」又は「腸まで届くタイプ」
カプセル数:60カプセル
会社のロゴと会社名:Mirel Oka
赤系
現在販売中のラクトフェリンのサプリの写真を添付します。
ロゴや商品名などの配置は同じにしなくてもよいです。
現在販売中のラクトフェリンサプリの画像をアップしました。
希望の色はピンク系でお願いします。

ナチュラル、オーガニックなイメージ、可愛いパケージで女性に好評であったためこのデザインを採用させて頂きました。

多くの提案をして頂きましてありがとうございました。
また、サプリやホームページのデザインをお願いする可能性がありますのでその際はよろしくお願いいたします。

```html
<!DOCTYPE html>
<html lang="ja">
<head>
<meta charset="utf-8">
<title>Mirel Oka クリスパタス菌+ガセリ菌</title>
<link href="https://fonts.googleapis.com/css2?family=M+PLUS+Rounded+1c:wght@500;700;800&display=swap" rel="stylesheet">
<style>
  :root{
    --pink:#f07fa6;
    --pink-soft:#fbd9e4;
    --pink-pale:#fdf0f5;
    --pink-mid:#f8c6d6;
    --band:#f6a9c2;
    --text:#5a4a52;
    --lavender:#b9b5dc;
    --lavender-text:#4d4a7a;
    --mark:#79c28a;
    --stomach-top:#ffffff;
    --stomach-bottom:#e6e1ea;
  }
  *{margin:0;padding:0;box-sizing:border-box}
  html,body{width:886px;height:1200px;overflow:hidden}
  body{font-family:"M PLUS Rounded 1c",sans-serif;color:var(--text);position:relative;
    background:radial-gradient(ellipse at 50% 45%, #fff 0%, var(--pink-pale) 40%, var(--pink-soft) 100%)}
  .decor-glow{position:absolute;left:93px;top:250px;width:700px;height:640px;border-radius:50%;
    background:radial-gradient(ellipse at 50% 50%, var(--pink-mid) 0%, rgba(248,198,214,0) 70%);opacity:.8}
  .category{position:absolute;top:110px;width:100%;text-align:center;font-size:40px;font-weight:700}
  .product-name{position:absolute;width:100%;text-align:center;font-weight:800;color:var(--pink);
    font-size:96px;line-height:1;letter-spacing:2px;
    text-shadow:4px 4px 0 #fff,-4px -4px 0 #fff,4px -4px 0 #fff,-4px 4px 0 #fff,0 4px 0 #fff,0 -4px 0 #fff,4px 0 0 #fff,-4px 0 0 #fff}
  .name-1{top:200px}
  .name-2{top:320px}
  .count-band{position:absolute;left:80px;right:80px;top:450px;height:80px;border-radius:40px;
    background:var(--band);color:#fff;text-align:center;font-size:50px;font-weight:800;line-height:80px}
  .pairing{position:absolute;top:560px;width:100%;text-align:center;font-size:36px;font-weight:700}
  .stomach{position:absolute;left:343px;top:640px;width:200px;height:290px;border-radius:24px;
    background:linear-gradient(180deg,var(--stomach-top),var(--stomach-bottom))}
  .brand{position:absolute;left:50px;top:960px;display:flex;flex-direction:column;align-items:flex-start;gap:14px}
  .brand-mark{width:80px;height:80px;background:var(--mark);border-radius:12px}
  .brand-name{font-size:36px;font-weight:700;line-height:1}
  .capsule-type{position:absolute;left:290px;top:1040px;width:340px;height:76px;border-radius:38px;
    background:var(--lavender);color:var(--lavender-text);font-size:46px;font-weight:800;text-align:center;line-height:76px}
  .capsule-count{position:absolute;left:680px;top:930px;width:150px;height:150px;border-radius:50%;
    background:var(--lavender);color:var(--lavender-text);text-align:center;font-weight:800}
  .capsule-count .num{display:block;font-size:64px;line-height:1;margin-top:28px}
  .capsule-count .unit{display:block;font-size:22px;margin-top:6px}
</style>
</head>
<body>
  <div class="decor-glow" role="img" aria-label="ハートの装飾"></div>
  <p class="category">健康補助食品</p>
  <h1 class="product-name name-1">クリスパタス菌</h1>
  <p class="product-name name-2">+ガセリ菌</p>
  <p class="count-band">〈生きた乳酸菌100億個〉</p>
  <p class="pairing">腸溶性と併用するのもおすすめ</p>
  <div class="stomach" role="img" aria-label="胃のイラスト"></div>
  <div class="brand">
    <span class="brand-mark"></span>
    <span class="brand-name">Mirel Oka</span>
  </div>
  <p class="capsule-type">胃で溶ける</p>
  <p class="capsule-count"><span class="num">60</span><span class="unit">カプセル</span></p>
</body>
</html>
```